Marlowe Ridge Holdings

I have a real estate investment business.

** I need editable vector files of the final design.

Industry/Entity Type

Real Estate

Contact Information for Business Card

I would like the card to be clear and direct with the company name and contact info. I would prefer not to have a design that is too busy (i.e., with excessive detail) in the business card.

Font styles to use
Sans Serif

Requirements
Must have
• My card must have the following information listed below:
• Company name: Marlowe Ridge Holdings LLC
• My name: Daniel Vestrap
• Phone number: (555) 218-9064
• Email address: dlvestrap@fernmail.example
• Keywords: “Real Estate Investments”
Nice to have
• I would like to have a design that resembles the characteristics/uses of obsidian stone which resembles something related to strength and resilience. Perhaps something with sharp, sleek color transitions as well.

```html
<!DOCTYPE html>
<html lang="en">
<head>
<meta charset="utf-8">
<title>Marlowe Ridge Holdings LLC — Business Card</title>
<link rel="stylesheet" href="https://fonts.googleapis.com/css2?family=Gelasio:wght@400&family=Oswald:wght@600&family=Lato:wght@400&display=swap">
<style>
  :root {
    --page-bg: #d9d9d7;
    --card-bg: #232323;
    --accent-blue: #2b9fdc;
    --text-light: #e6e6e6;
    --divider: #2b6e94;
  }
  * { box-sizing: border-box; margin: 0; padding: 0; }
  html, body {
    width: 1200px;
    height: 1200px;
    overflow: hidden;
    background: var(--page-bg);
  }
  .sheet {
    width: 1200px;
    height: 1200px;
    display: flex;
    flex-direction: column;
    align-items: center;
    justify-content: center;
    gap: 60px;
  }
  .card {
    position: relative;
    width: 900px;
    height: 514px;
    background: var(--card-bg);
    box-shadow: 0 10px 30px rgba(0,0,0,0.25);
  }
  /* Front */
  .card-front {
    display: flex;
    align-items: center;
    justify-content: center;
  }
  .company-name {
    font-family: "Gelasio", Georgia, serif;
    font-weight: 400;
    font-size: 58px;
    letter-spacing: 1px;
    color: var(--accent-blue);
  }
  /* Back */
  .card-back {
    border-bottom: 6px solid var(--accent-blue);
  }
  .identity-row {
    position: absolute;
    left: 150px;
    top: 215px;
    display: flex;
    align-items: center;
    gap: 30px;
  }
  .person-name {
    font-family: "Oswald", "Arial Narrow", sans-serif;
    font-weight: 600;
    font-size: 50px;
    letter-spacing: 1px;
    color: var(--accent-blue);
    text-transform: uppercase;
  }
  .divider {
    width: 1.5px;
    height: 60px;
    background: var(--divider);
  }
  .contact-list {
    list-style: none;
    display: flex;
    flex-direction: column;
    gap: 4px;
    font-family: "Lato", Arial, sans-serif;
    font-size: 20px;
    color: var(--text-light);
  }
  .contact-item {
    display: flex;
    align-items: center;
    gap: 10px;
  }
  .contact-icon { width: 16px; height: 16px; fill: var(--accent-blue); }
  .tagline {
    position: absolute;
    left: 490px;
    top: 430px;
    font-family: "Lato", Arial, sans-serif;
    font-size: 22px;
    color: var(--text-light);
    letter-spacing: 0.3px;
  }
</style>
</head>
<body>
  <main class="sheet">
    <section class="card card-front" aria-label="Card front">
      <h1 class="company-name">Marlowe Ridge Holdings LLC</h1>
    </section>

    <section class="card card-back" aria-label="Card back">
      <div class="identity-row">
        <h2 class="person-name">Daniel Vestrap</h2>
        <span class="divider"></span>
        <ul class="contact-list">
          <li class="contact-item">
            <svg class="contact-icon" viewBox="0 0 24 24" aria-hidden="true"><path d="M6.6 10.8a15.1 15.1 0 0 0 6.6 6.6l2.2-2.2a1 1 0 0 1 1-.25 11.4 11.4 0 0 0 3.6.57 1 1 0 0 1 1 1V20a1 1 0 0 1-1 1A17 17 0 0 1 3 4a1 1 0 0 1 1-1h3.5a1 1 0 0 1 1 1c0 1.25.2 2.45.57 3.57a1 1 0 0 1-.25 1z"/></svg>
            <span>+(555) 218-9064</span>
          </li>
          <li class="contact-item">
            <svg class="contact-icon" viewBox="0 0 24 24" aria-hidden="true"><path d="M2 5h20v14H2z M2 5l10 8 10-8" /></svg>
            <span>dlvestrap@fernmail.example</span>
          </li>
        </ul>
      </div>
      <p class="tagline">Real Estate Investments</p>
    </section>
  </main>
</body>
</html>
```